Trade Show Booth Sign Design for Retracting Banner

I need a trade show booth sign designed. It will be for a retractable banner that is double sided with 34 by 81 inch.

I want to incorporate my logo (see attached, have it in other file formats as well) and graphics from my website (https://www.dolbrookteachingadvisory.com/) with parts or all of the following text.

· Educational Content Creation
o Supplemental Textbook Content Development
o E-learning Content Development
· Curriculum Development
o KVTR/Bright Ladder
o Three Dimensional Learning
· Assessment
o Formative Assessments
o Elementary School, Middle School, High School, College, and Business
· Professional Development
o Training
o Facilitation

Target Market(s)

Education

Industry/Entity Type

Education

Font styles to use
Sans Serif

Colors

Designer to choose colors to be used in the design.

Requirements
Must have
• Eye catching and easy to read design
Nice to have
• Would like to see incorporation of my logo and some of the elements of my website images
Should not have
• N/A

```html
<!DOCTYPE html>
<html lang="en">
<head>
<meta charset="utf-8">
<title>Dolbrook Teaching Advisory – Retractable Banner</title>
<link href="https://fonts.googleapis.com/css2?family=Montserrat:wght@400;500;700;800&display=swap" rel="stylesheet">
<style>
:root{
  --navy:#1f2a6b;
  --blue:#263a7a;
  --blue-deep:#1d2452;
  --charcoal:#2f2f2f;
  --white:#ffffff;
  --lime:#e1ea86;
  --page:#ffffff;
}
*{margin:0;padding:0;box-sizing:border-box}
html,body{width:1200px;height:1200px;overflow:hidden;background:var(--page);font-family:'Montserrat',sans-serif}
.banner{position:absolute;left:363px;top:34px;width:475px;height:1132px;background:var(--blue-deep);overflow:hidden}
.banner__topline{position:absolute;left:0;top:0;width:100%;height:6px;background:var(--navy)}
.brand{position:absolute;left:0;top:6px;width:100%;height:80px;background:var(--white);display:flex;flex-direction:column;align-items:center;justify-content:center;color:var(--navy);font-weight:800;line-height:1}
.brand__name{font-size:40px;letter-spacing:-1px}
.brand__tag{font-size:13px;margin-top:3px;letter-spacing:.5px}
.brand__rule{position:absolute;left:0;top:86px;width:100%;height:8px;background:var(--navy)}
.hero{position:absolute;left:0;top:94px;width:100%;height:232px}
.hero__art{position:absolute;left:0;top:0;width:100%;height:150px;background:radial-gradient(circle at 50% 55%,#4a4a3a 0%,#333 45%,#2b2b2b 100%)}
.hero__title{position:absolute;left:0;top:148px;width:100%;text-align:center;color:var(--white);font-weight:700;font-size:21.5px;letter-spacing:.2px}
.field{position:absolute;left:0;top:0}
.service__icon{position:absolute;width:64px;height:64px;border-radius:50%;border:2px solid #c9cde0;background:radial-gradient(circle,#2d4a8c 0%,#1c2656 100%)}
.service__title{position:absolute;left:104px;color:var(--white);font-weight:800;font-size:30px;line-height:28px}
.service__title--light{font-weight:700}
.service__list{position:absolute;left:84px;list-style:none;color:var(--lime);font-weight:500;font-size:20px;line-height:21px}
.service__list li{position:relative;padding-left:20px}
.service__list li::before{content:"";position:absolute;left:0;top:4px;border-left:12px solid var(--white);border-top:7px solid transparent;border-bottom:7px solid transparent}
.contact{position:absolute;right:58px;top:948px;text-align:right;color:var(--white);font-size:13.5px;line-height:20.5px}
.contact__head{display:inline-block;font-weight:700;font-size:14px;border-bottom:1.5px solid var(--white);padding-bottom:2px;margin-bottom:5px;margin-right:-20px}
.contact__row{display:flex;justify-content:flex-end;align-items:center;gap:8px;margin-right:-28px}
.contact__row svg{width:17px;height:17px;flex:none}
.footer__line{position:absolute;left:0;top:1058px;width:100%;height:5px;background:var(--white)}
.footer{position:absolute;left:0;top:1063px;width:100%;height:69px;background:var(--charcoal);color:var(--white);font-size:23px;font-weight:500;display:flex;align-items:center;justify-content:center}
</style>
</head>
<body>
<main class="banner">
  <div class="banner__topline"></div>
  <header class="brand">
    <span class="brand__name">DOLBROOK</span>
    <span class="brand__tag">Teaching Advisory</span>
  </header>
  <div class="brand__rule"></div>

  <svg class="field" width="475" height="1132" viewBox="0 0 475 1132" aria-hidden="true">
    <rect x="0" y="300" width="475" height="760" fill="var(--blue-deep)"/>
    <polygon points="0,300 475,300 475,565 340,735 0,330" fill="var(--blue)"/>
    <polygon points="0,330 340,735 250,850 0,560" fill="#22316b"/>
    <polygon points="0,560 250,850 150,980 0,820" fill="#1f2a5e"/>
  </svg>

  <section class="hero">
    <div class="hero__art" role="img" aria-label="Crumpled paper light bulbs in red, blue, yellow, orange and light blue hanging on a chalkboard, the centre one glowing"></div>
    <h1 class="hero__title">DOLBROOK TEACHING ADVISORY</h1>
    <svg width="475" height="232" viewBox="0 0 475 232" style="position:absolute;left:0;top:0" aria-hidden="true">
      <path d="M0,192 L237.5,212 L475,192 L475,232 L0,232 Z" fill="var(--white)"/>
      <path d="M0,200 L237.5,224 L475,200 L475,232 L0,232 Z" fill="var(--blue)"/>
    </svg>
  </section>

  <div class="service__icon" style="left:22px;top:369px" role="img" aria-label="Graduation cap above a light bulb with a brain"></div>
  <h2 class="service__title" style="top:374px">Educational<br><span class="service__title--light">Content Creation</span></h2>
  <ul class="service__list" style="top:443px">
    <li>Supplemental Textbook Content</li>
    <li>E-learning Content Development</li>
  </ul>

  <div class="service__icon" style="left:22px;top:504px" role="img" aria-label="Teacher presenting charts on a whiteboard to a class"></div>
  <h2 class="service__title" style="top:508px">Curriculum<br><span class="service__title--light">Development</span></h2>
  <ul class="service__list" style="top:580px">
    <li>KVTR/Bright Ladder</li>
    <li>Three Dimensional Learning</li>
  </ul>

  <div class="service__icon" style="left:22px;top:640px" role="img" aria-label="Science flask surrounded by small education symbols"></div>
  <h2 class="service__title" style="top:660px;left:106px">Assessment</h2>
  <ul class="service__list" style="top:702px">
    <li>Formative Assessments</li>
    <li>Elementary School, Middle School,<br>High School, College, and Business</li>
  </ul>

  <div class="service__icon" style="left:22px;top:776px" role="img" aria-label="Presenter leading a training session in front of seated attendees"></div>
  <h2 class="service__title" style="top:780px">Professional<br><span class="service__title--light">Development</span></h2>
  <ul class="service__list" style="top:852px">
    <li>Training</li>
    <li>Facilitation</li>
  </ul>

  <address class="contact" style="font-style:normal">
    <div class="contact__head">CONTACT US</div>
    <div class="contact__row">555.014.2290
      <svg viewBox="0 0 20 20"><circle cx="10" cy="10" r="8.5" fill="none" stroke="#fff" stroke-width="1.5"/><path d="M7 5.5l1.6 2.4-1 1.2c.6 1.3 1.6 2.3 2.9 2.9l1.2-1 2.4 1.6-.8 1.7c-3.5.2-7.6-3.9-7.4-7.4z" fill="#fff"/></svg>
    </div>
    <div class="contact__row">mdolbrook@dolbrookteachingadvisory.com
      <svg viewBox="0 0 20 20"><circle cx="10" cy="10" r="8.5" fill="none" stroke="#fff" stroke-width="1.5"/><rect x="5.5" y="7" width="9" height="6.5" rx="1" fill="#fff"/><path d="M5.8 7.4L10 10.6l4.2-3.2" fill="none" stroke="var(--blue-deep)" stroke-width="1"/></svg>
    </div>
    <div class="contact__row">1280 Alder Creek Lane, Fernhill Ohio 44012
      <svg viewBox="0 0 20 20"><circle cx="10" cy="10" r="8.5" fill="none" stroke="#fff" stroke-width="1.5"/><path d="M10 15s-3.5-3.6-3.5-6.2a3.5 3.5 0 0 1 7 0C13.5 11.4 10 15 10 15z" fill="#fff"/><circle cx="10" cy="8.8" r="1.3" fill="var(--blue-deep)"/></svg>
    </div>
  </address>

  <div class="footer__line"></div>
  <footer class="footer">www.dolbrookteachingadvisory.com</footer>
</main>
</body>
</html>
```